Real Estate investment company needs billboard designs

This is our website: https://velmarkpropertygroup.com/
We are looking for some billboard concepts that uses our CEO in the design. I have attached some images and 1 billboard design that someone in our industry uses, but we don't want it exactly like his.

Industry/Entity Type

real estate

Colors

Designer to choose colors to be used in the design.

Requirements
Must have
• Company colors from websiute

```html
<!DOCTYPE html>
<html lang="en">
<head>
<meta charset="utf-8">
<title>Velmark Property Group – Billboard</title>
<link href="https://fonts.googleapis.com/css2?family=Montserrat:wght@600;700;800;900&display=swap" rel="stylesheet">
<style>
  :root {
    --page-bg: #d9d9d9;
    --navy: #1b1b3d;
    --navy-deep: #121230;
    --red: #e3161c;
    --red-dark: #7a0f1a;
    --yellow: #fdd71f;
    --yellow-deep: #f5b800;
    --white: #ffffff;
    --denim: #8fa6c4;
    --denim-dark: #5e7597;
  }
  * { margin: 0; padding: 0; box-sizing: border-box; }
  html, body {
    width: 1031px; height: 1200px; overflow: hidden;
    background: var(--page-bg);
    font-family: "Montserrat", Arial, sans-serif;
  }
  .billboard {
    position: absolute; left: 25px; top: 373px;
    width: 980px; height: 453px; overflow: hidden;
    background: linear-gradient(120deg, var(--navy) 0%, var(--navy-deep) 100%);
    box-shadow: 0 10px 24px rgba(0,0,0,0.35);
  }
  .billboard__chevron { position: absolute; inset: 0; width: 980px; height: 453px; }
  .ceo-photo {
    position: absolute; left: 722px; top: 58px; width: 258px; height: 395px;
    border-radius: 120px 120px 0 0;
    background: radial-gradient(ellipse at 45% 22%, #c89a82 0%, #b48a75 20%, var(--denim) 42%, var(--denim-dark) 100%);
    z-index: 1;
  }
  .headline {
    position: absolute; left: 36px; top: 40px; z-index: 3;
    color: var(--white); font-weight: 800; font-size: 98px;
    line-height: 98px; letter-spacing: -1px; text-transform: uppercase;
    white-space: nowrap;
  }
  .brand {
    position: absolute; left: 43px; top: 276px; z-index: 3;
    display: flex; align-items: center; gap: 10px;
  }
  .brand__square { width: 22px; height: 22px; background: var(--red); }
  .brand__name {
    color: var(--white); font-weight: 700; font-size: 22px; letter-spacing: 0.5px;
  }
  .web-band {
    position: absolute; left: 0; top: 347px; width: 640px; height: 57px; z-index: 2;
    background: linear-gradient(90deg, var(--red) 0%, var(--red) 45%, rgba(227,22,28,0.35) 80%, rgba(227,22,28,0) 100%);
    display: flex; align-items: center; padding-left: 44px; gap: 17px;
  }
  .web-band__icon { width: 26px; height: 26px; flex: none; }
  .web-band__url {
    color: var(--white); font-weight: 700; font-size: 24px; text-decoration: none;
  }
  .badge { position: absolute; left: 512px; top: 152px; width: 174px; height: 174px; z-index: 2; }
  .badge__text {
    position: absolute; left: 545px; top: 193px; z-index: 3;
    font-weight: 800; font-size: 24px; line-height: 30px; color: var(--navy);
  }
  .badge__text .accent { color: var(--red); }
</style>
</head>
<body>
  <section class="billboard">
    <svg class="billboard__chevron" viewBox="0 0 980 453" aria-hidden="true">
      <defs>
        <linearGradient id="chevronRed" x1="0" y1="0" x2="0.4" y2="1">
          <stop offset="0" stop-color="#7a0f1a"/>
          <stop offset="0.5" stop-color="#e3161c"/>
          <stop offset="1" stop-color="#e3161c"/>
        </linearGradient>
      </defs>
      <polygon points="595,0 765,0 953,214 713,453 578,453 818,214" fill="url(#chevronRed)"/>
    </svg>

    <div class="ceo-photo" role="img" aria-label="Photo of the company CEO in a denim shirt, smiling and pointing up"></div>

    <h1 class="headline">Guranteed<br>Offer</h1>

    <div class="brand">
      <span class="brand__square"></span>
      <span class="brand__name">VELMARK PROPERTY GROUP</span>
    </div>

    <div class="web-band">
      <svg class="web-band__icon" viewBox="0 0 26 26" aria-hidden="true">
        <circle cx="13" cy="13" r="11" fill="none" stroke="#1b1b3d" stroke-width="2.4"/>
        <ellipse cx="13" cy="13" rx="5" ry="11" fill="none" stroke="#1b1b3d" stroke-width="2"/>
        <line x1="2" y1="13" x2="24" y2="13" stroke="#1b1b3d" stroke-width="2"/>
      </svg>
      <a class="web-band__url" href="https://velmarkpropertygroup.com/">velmarkpropertygroup.com</a>
    </div>

    <svg class="badge" viewBox="0 0 180 180" aria-hidden="true">
      <defs>
        <radialGradient id="badgeYellow" cx="0.4" cy="0.35" r="0.7">
          <stop offset="0" stop-color="#fdd71f"/>
          <stop offset="1" stop-color="#f5b800"/>
        </radialGradient>
      </defs>
      <circle cx="90" cy="90" r="80" fill="url(#badgeYellow)"/>
      <circle cx="90" cy="90" r="80" fill="none" stroke="url(#badgeYellow)" stroke-width="16"
              stroke-linecap="round" pathLength="24" stroke-dasharray="0 1"/>
    </svg>
    <div class="badge__text">LIMITED<br>TIME<br><span class="accent">ONLY!</span></div>
  </section>
</body>
</html>
```